"Got Radon?" Banner Ads

I need banner ads made for Pelvaro Banner Circuit campaign. There are 10 sizes of banners, so I need all 10 sizes. All of them can be similar in design and concept, but need to look good and the content must fill the space nicely.

The text on the ad is "Got Radon?" big/bold, and there should be a picture of a house with gas seeping into it from the ground. I have attached an example of an existing ad for reference.

These are the 10 sizes of banners that we need:
970x90
120x600
160x600
200x200
250x250
350x250
300x600
336x280
468x60
728x90

```html
<!DOCTYPE html>
<html lang="en">
<head>
<meta charset="utf-8">
<title>Got Radon? Banner Set</title>
<link href="https://fonts.googleapis.com/css2?family=Bebas+Neue&display=swap" rel="stylesheet">
<style>
:root{
  --green:#1f8a14;
  --black:#000;
  --white:#fff;
  --grey:#dadada;
  --grey-light:#e4e4e4;
  --yellow:#f5d33c;
  --lime:#d6f23a;
}
*{margin:0;padding:0;box-sizing:border-box}
html,body{width:1200px;height:800px;overflow:hidden;background:var(--white)}
body{position:relative;font-family:"Bebas Neue",sans-serif;color:var(--black);line-height:.9}
.ad,.block{position:absolute;overflow:hidden}
.grey{background:linear-gradient(180deg,var(--grey-light),var(--grey))}
.green-bg{background:var(--green)}
.black-bg{background:var(--black)}
.photo{position:absolute;background:linear-gradient(180deg,#4d8fc9 0%,#9cc6e6 30%,#b8583a 48%,#e9ecef 62%,#c5c9cc 74%,#5f8a3a 86%,#4c7a2c 100%)}
.hl{position:absolute;white-space:nowrap}
.g{color:var(--green)}
.w{color:var(--white)}
.btn{position:absolute;display:flex;align-items:center;justify-content:center;border-radius:3px;white-space:nowrap}
.btn-green{background:var(--green);color:var(--white)}
.btn-black{background:var(--black);color:var(--white)}
.btn-light{background:var(--grey-light);color:var(--green)}
.phone{position:absolute;white-space:nowrap}
.perks{position:absolute;white-space:nowrap;word-spacing:2px}
</style>
</head>
<body>

<!-- 970x90 leaderboard -->
<section class="ad leaderboard" style="left:22px;top:22px;width:964px;height:88px">
  <div class="block black-bg" style="left:0;top:0;width:455px;height:88px"></div>
  <div class="hl w" style="left:26px;top:6px;font-size:104px">GOT RADON?</div>
  <div class="photo" role="img" aria-label="House with radon gas seeping from the ground" style="left:455px;top:0;width:139px;height:88px"></div>
  <div class="block grey" style="left:594px;top:0;width:370px;height:88px"></div>
  <div class="btn btn-black" style="left:602px;top:23px;width:106px;height:32px;font-size:21px">CLICK HERE</div>
  <div class="phone g" style="left:720px;top:18px;font-size:44px">1-800-<span style="color:var(--black)">AIR-SAFE</span></div>
  <div class="perks" style="left:602px;top:70px;font-size:15px">FREE ESTIMATES &nbsp;| &nbsp;SAME DAY SERVICE &nbsp;| &nbsp;BEST PRICE GUARANTEE</div>
</section>
<div class="block" style="left:1000px;top:22px;width:182px;height:88px;background:var(--yellow)"></div>

<!-- 120x600 skyscraper -->
<section class="ad grey" style="left:23px;top:122px;width:106px;height:528px">
  <div class="block green-bg" style="left:0;top:0;width:106px;height:91px"></div>
  <div class="hl" style="left:0;width:106px;text-align:center;top:122px;font-size:43px">GOT</div>
  <div class="hl g" style="left:0;width:106px;text-align:center;top:160px;font-size:42px">RADON?</div>
  <div class="photo" role="img" aria-label="House with radon gas seeping from the ground" style="left:0;top:222px;width:106px;height:71px"></div>
  <div class="btn btn-green" style="left:13px;top:397px;width:80px;height:25px;font-size:15px">CLICK HERE</div>
  <div class="phone" style="left:0;width:106px;text-align:center;top:506px;font-size:16px"><span class="g">1-800-</span>AIR-SAFE</div>
</section>

<!-- 160x600 skyscraper -->
<section class="ad grey" style="left:138px;top:122px;width:141px;height:528px">
  <div class="block green-bg" style="left:0;top:0;width:141px;height:91px"></div>
  <div class="hl" style="left:0;width:141px;text-align:center;top:113px;font-size:54px">GOT</div>
  <div class="hl g" style="left:0;width:141px;text-align:center;top:162px;font-size:52px">RADON?</div>
  <div class="photo" role="img" aria-label="House with radon gas seeping from the ground" style="left:0;top:225px;width:141px;height:97px"></div>
  <div class="btn btn-green" style="left:20px;top:411px;width:102px;height:34px;font-size:21px">CLICK HERE</div>
  <div class="phone" style="left:0;width:141px;text-align:center;top:503px;font-size:25px"><span class="g">1-800-</span>AIR-SAFE</div>
</section>

<!-- 250x250 square -->
<section class="ad grey" style="left:287px;top:122px;width:304px;height:304px">
  <div class="photo" role="img" aria-label="House with radon gas seeping from the ground" style="left:0;top:0;width:304px;height:202px"></div>
  <div class="hl" style="left:2px;top:218px;font-size:78px">GOT <span class="g">RADON?</span></div>
</section>

<!-- 200x200 small square -->
<section class="ad grey" style="left:602px;top:122px;width:270px;height:270px">
  <div class="photo" role="img" aria-label="House with radon gas seeping from the ground" style="left:0;top:0;width:270px;height:183px"></div>
  <div class="hl" style="left:8px;top:200px;font-size:67px">GOT <span class="g">RADON?</span></div>
</section>
<div class="block black-bg" style="left:886px;top:122px;width:20px;height:270px"></div>

<!-- 300x600 half page -->
<section class="ad grey" style="left:914px;top:120px;width:268px;height:534px">
  <div class="photo" role="img" aria-label="House with radon gas seeping from the ground" style="left:0;top:0;width:268px;height:179px"></div>
  <div class="hl" style="left:15px;top:206px;font-size:100px">GOT</div>
  <div class="hl g" style="left:15px;top:288px;font-size:98px">RADON?</div>
  <div class="btn btn-black" style="left:18px;top:399px;width:229px;height:69px;font-size:44px">CLICK HERE</div>
  <div class="phone" style="left:0;width:268px;text-align:center;top:485px;font-size:44px"><span class="g">1-800-</span>AIR-SAFE</div>
</section>

<!-- 350x250 rectangle -->
<section class="ad" style="left:287px;top:437px;width:304px;height:215px">
  <div class="block grey" style="left:0;top:0;width:122px;height:122px"></div>
  <div class="hl" style="left:10px;top:34px;font-size:43px;line-height:.88">GOT<br>RADON?</div>
  <div class="photo" role="img" aria-label="House with radon gas seeping from the ground" style="left:122px;top:0;width:182px;height:122px"></div>
  <div class="block green-bg" style="left:0;top:122px;width:304px;height:93px"></div>
  <div class="phone w" style="left:10px;top:148px;font-size:31px">1-800-<span style="color:var(--black)">AIR-SAFE</span></div>
  <div class="btn btn-light" style="left:193px;top:146px;width:102px;height:31px;font-size:19px">CLICK HERE</div>
  <div class="perks" style="left:10px;top:197px;font-size:13px;color:var(--lime)">FREE ESTIMATES &nbsp;| &nbsp;SAME DAY SERVICE &nbsp;| &nbsp;BEST PRICE GUARANTEE</div>
</section>

<!-- 336x280 large rectangle -->
<section class="ad" style="left:601px;top:400px;width:305px;height:252px">
  <div class="block grey" style="left:0;top:0;width:122px;height:122px"></div>
  <div class="hl" style="left:10px;top:27px;font-size:43px;line-height:.88">GOT<br>RADON?</div>
  <div class="photo" role="img" aria-label="House with radon gas seeping from the ground" style="left:122px;top:0;width:183px;height:122px"></div>
  <div class="block green-bg" style="left:0;top:122px;width:305px;height:105px"></div>
  <div class="btn btn-light" style="left:101px;top:149px;width:103px;height:32px;font-size:19px">CLICK HERE</div>
  <div class="perks w" style="left:7px;top:200px;font-size:13px">FREE ESTIMATES &nbsp;| &nbsp;SAME DAY SERVICE &nbsp;| &nbsp;BEST PRICE GUARANTEE</div>
  <div class="block grey" style="left:0;top:227px;width:305px;height:25px"></div>
  <div class="phone" style="left:0;width:305px;text-align:center;top:228px;font-size:25px;letter-spacing:4px"><span class="g">1-800-</span>AIR-SAFE</div>
</section>

<!-- 728x90 wide banner -->
<section class="ad grey" style="left:23px;top:663px;width:447px;height:55px">
  <div class="hl" style="left:13px;top:6px;font-size:57px">GOT RADON?</div>
  <div class="photo" role="img" aria-label="House with radon gas seeping from the ground" style="left:241px;top:0;width:101px;height:55px"></div>
  <div class="block green-bg" style="left:342px;top:0;width:105px;height:55px"></div>
  <div class="btn btn-black" style="left:356px;top:17px;width:77px;height:23px;font-size:14px">CLICK HERE</div>
</section>
<div class="block black-bg" style="left:478px;top:663px;width:290px;height:55px"></div>

<!-- 468x60 banner -->
<section class="ad grey" style="left:778px;top:663px;width:404px;height:52px">
  <div class="hl" style="left:12px;top:6px;font-size:50px">GOT RADON?</div>
  <div class="photo" role="img" aria-label="House with radon gas seeping from the ground" style="left:218px;top:0;width:82px;height:52px"></div>
  <div class="block green-bg" style="left:300px;top:0;width:104px;height:52px"></div>
  <div class="btn btn-black" style="left:315px;top:15px;width:74px;height:23px;font-size:15px">CLICK HERE</div>
</section>

<div class="block green-bg" style="left:22px;top:729px;width:1160px;height:49px"></div>

</body>
</html>
```